Webseite für Klempnerei Wendlin GmbH
Zielgruppe
Traditionsreicher Familienbetrieb: Klempnerei für Heizung, Bäder nach Maß und Sanitär, Dachklempnerei, Solar, alternative Energien
Aufgabenstellung
Die Farben der Webseite sollen bitte die gleichen, wie auf der alten Seite sein.
Also blau mit Akzenten in vorwiegend rot und ein wenig gelb.
Insgesamt soll die Webseite klar strukturiert sein, aber dennoch modern wirken.
Die Navigationsleiste bitte in folgender Reihenfolge:
-Start
- Das sind wir
-Leistungsübersicht
- Referenzen
- aktuelle Meldungen
- Kontakt
Die Startseite soll wie folgt gestaltet sein und Call to action wahllos in der Startseite evrteilen:
- großes Headerbild
-Teaser zu' Das sind wir' - Familientradition betonen
- Leistungsübersicht in Boxen mit großem Bild und angedeuteter Verlinkung zu der Leistungsunterseite: Heizung, Bäder nach Maß, Dachklempnerei, Solar, alternative Energien
-Teaser zu Referenzen
- Teaser zu aktuelle Meldungen
- Kontakt mit Map
- Footer mit Aufführung: Mitglied der Innung
-Datenschutz und Impressum
Bei den Inhalten bitte an der alten Webseite orientieren: https://www.heizung-wendlin.example/#
Bilder bitte entsprechende Vorschlagen

```html
<!DOCTYPE html>
<html lang="de">
<head>
<meta charset="utf-8">
<title>Klempnerei Wendlin GmbH – Startseite</title>
<link href="https://fonts.googleapis.com/css2?family=Arimo:wght@400;700&family=Montserrat:wght@500;600;700&display=swap" rel="stylesheet">
<style>
:root{
  --board:#f2f2f2;
  --white:#ffffff;
  --ink:#2b2b2b;
  --ink-soft:#444444;
  --brand-blue:#3a4aa6;
  --brand-blue-deep:#2c3a8c;
  --navy:#24384f;
  --navy-deep:#1b2c3e;
  --hero-a:#4b5da3;
  --hero-b:#2a4258;
  --rule:#9a9a9a;
  --veil:rgba(255,255,255,.22);
}
*{margin:0;padding:0;box-sizing:border-box}
html,body{width:1200px;height:1200px;overflow:hidden;background:var(--board)}
body{font-family:"Arimo",Arial,sans-serif;color:var(--ink)}
.board{position:relative;width:1200px;height:1200px;overflow:hidden;background:var(--board)}
.abs{position:absolute}
.page{position:absolute;background:var(--white);box-shadow:0 6px 18px rgba(0,0,0,.18);overflow:hidden}

/* shared */
.wordmark{font-family:"Arimo",Arial,sans-serif;font-weight:700;color:var(--brand-blue);display:flex;align-items:center;white-space:nowrap}
.wordmark .dot{border-radius:50%;background:var(--brand-blue);display:inline-block}
.nav-item{font-family:"Montserrat",sans-serif;font-weight:600;color:var(--ink);letter-spacing:.22em;white-space:nowrap;position:absolute}
.burger span{display:block;background:var(--ink)}
.photo{position:absolute}
.spaced{letter-spacing:.14em}
.tag{position:absolute;background:var(--brand-blue);color:var(--white);letter-spacing:.14em;white-space:nowrap}
.social{position:absolute;background:var(--white);border-radius:1px}

/* ===== full desktop page ===== */
.desk{left:383px;top:42px;width:704px;height:1158px}
.desk .header{position:absolute;left:0;top:0;width:704px;height:52px;background:var(--white)}
.desk .wordmark{left:44px;top:10px;font-size:21px;gap:5px}
.desk .wordmark .dot{width:15px;height:15px}
.desk .tagline{position:absolute;left:44px;top:32px;font-size:6.6px;font-weight:700;color:var(--brand-blue);letter-spacing:.02em}
.desk .nav-item{top:23px;font-size:6.6px}
.desk .nav-item.is-active{border-bottom:1px solid var(--ink);padding-bottom:1px}
.desk .burger{position:absolute;left:675px;top:20px;width:13px}
.desk .burger span{height:1.2px;margin-bottom:4px}

.desk .hero{position:absolute;left:0;top:52px;width:704px;height:346px;color:var(--white);text-align:center}
.desk .hero-photo{left:0;top:0;width:704px;height:346px;background:linear-gradient(100deg,var(--hero-a) 0%,#51639b 35%,#3c5370 65%,var(--hero-b) 100%)}
.desk .kicker{position:absolute;left:0;width:704px;top:67px;font-family:"Montserrat",sans-serif;font-weight:700;font-size:8px;letter-spacing:.09em}
.desk .title-line{position:absolute;background:var(--veil);font-size:26px;letter-spacing:.22em;line-height:33px;height:33px;text-align:center;white-space:nowrap;font-weight:400}
.desk .hero-sub{position:absolute;left:0;width:704px;top:210px;font-size:9.4px;line-height:12.5px;letter-spacing:.08em}
.desk .btn-hero{position:absolute;left:296px;top:256px;width:119px;height:29px;background:var(--white);color:var(--ink);font-family:"Montserrat",sans-serif;font-weight:700;font-size:8px;letter-spacing:.2em;line-height:29px;text-align:center}
.desk .social{left:676px;width:8px;height:8px}

.desk .h-box{position:absolute;background:rgba(255,255,255,.93);box-shadow:0 1px 3px rgba(0,0,0,.12);font-size:18.5px;letter-spacing:.16em;line-height:28px;height:28px;padding-left:7px;white-space:nowrap;color:var(--ink)}
.desk .body{position:absolute;font-size:8.4px;line-height:11.35px;letter-spacing:.06em;color:var(--ink-soft)}
.desk .body p+p{margin-top:11.35px}
.desk .divider{position:absolute;left:0;top:746px;width:289px;height:1px;background:var(--rule)}
.desk .h-meister{position:absolute;left:392px;top:785px;font-size:21px;line-height:28.5px;letter-spacing:.14em;color:var(--ink)}
.desk .arrow{position:absolute;width:22px;height:22px}
.desk .tag{font-size:14.5px;height:23px;line-height:23px;padding-left:11px}
.desk .dots{position:absolute;left:184px;top:1105px;display:flex;gap:2px}
.desk .dots i{width:5px;height:5px;border-radius:50%;border:.8px solid var(--brand-blue);display:block}
.desk .dots i.on{background:var(--brand-blue)}

/* ===== mobile-scale overview page ===== */
.strip{left:75px;top:49px;width:234px;height:1102px}
.strip .band{position:absolute;left:0;width:234px}
.strip .wordmark{left:14px;top:3px;font-size:7px;gap:2px}
.strip .wordmark .dot{width:5px;height:5px}
.strip .tagline{position:absolute;left:14px;top:11px;font-size:2.2px;font-weight:700;color:var(--brand-blue)}
.strip .nav-item{top:7px;font-size:2.2px;letter-spacing:.12em}
.strip .burger{position:absolute;left:225px;top:6px;width:5px}
.strip .burger span{height:.5px;margin-bottom:1.3px}
.strip .c{text-align:center;left:0;width:234px}
.strip .tx{position:absolute;font-size:2.6px;line-height:3.5px;letter-spacing:.03em;color:var(--ink-soft)}
.strip .tx p+p{margin-top:3.5px}
.strip .hbox{position:absolute;background:rgba(255,255,255,.92);box-shadow:0 .5px 1px rgba(0,0,0,.15);font-size:5.6px;letter-spacing:.13em;line-height:8.5px;height:8.5px;padding-left:2px;white-space:nowrap;color:var(--ink)}
.strip .veil-line{position:absolute;background:var(--veil);color:var(--white);font-size:7.6px;letter-spacing:.2em;line-height:10px;height:10px;text-align:center;white-space:nowrap}
.strip .hd{position:absolute;font-size:6.7px;line-height:8.6px;letter-spacing:.12em;color:var(--ink)}
.strip .tag{font-size:4.7px;height:7.5px;line-height:7.5px;padding-left:4px}
.strip .ring{position:absolute;width:7px;height:7px;border-radius:50%;border:.5px solid var(--ink);font-size:4px;line-height:6px;text-align:center}
.strip .btn{position:absolute;font-family:"Montserrat",sans-serif;font-weight:700;font-size:2.6px;letter-spacing:.15em;text-align:center}
.strip .field{position:absolute;background:rgba(255,255,255,.88);font-size:2.5px;padding:1.2px 2px;color:var(--ink)}
.strip .side-tab{position:absolute;left:198px;width:36px;height:5.5px;background:var(--brand-blue);color:var(--white);font-size:2.2px;line-height:5.5px;padding-left:2px;border-bottom:.6px solid rgba(255,255,255,.35)}
.strip .white{color:var(--white)}
</style>
</head>
<body>
<div class="board">

  <!-- ============ overview page ============ -->
  <section class="page strip" aria-label="Startseite Gesamtansicht">
    <header class="band" style="top:0;height:17px;background:var(--white)">
      <div class="wordmark abs"><span class="dot"></span>wendlin</div>
      <div class="tagline">Heizung · Sanitär · Bauklempnerei</div>
      <span class="nav-item" style="left:82px;border-bottom:.4px solid var(--ink)">HOME</span>
      <span class="nav-item" style="left:101px">ÜBER UNS</span>
      <span class="nav-item" style="left:124px">LEISTUNGEN</span>
      <span class="nav-item" style="left:151px">AKTUELL</span>
      <span class="nav-item" style="left:172px">REFERENZEN</span>
      <span class="nav-item" style="left:198px">KONTAKT</span>
      <div class="burger"><span></span><span></span><span></span></div>
    </header>

    <div class="band" style="top:17px;height:115px">
      <div class="photo" role="img" aria-label="Headerbild: modernes Badezimmer mit Waschtisch, blau getönt" style="left:0;top:0;width:234px;height:115px;background:linear-gradient(100deg,var(--hero-a),#4d5f98 40%,var(--hero-b))"></div>
      <div class="abs c white" style="top:24px;font-family:Montserrat,sans-serif;font-weight:700;font-size:2.7px;letter-spacing:.08em">TRADITIONSREICHER FAMILIENBETRIEB:</div>
      <div class="veil-line" style="left:47px;top:30px;width:135px">Willkommen bei wendlin</div>
      <div class="veil-line" style="left:47px;top:43px;width:135px">Ihr Experte für Heizung,</div>
      <div class="veil-line" style="left:38px;top:56px;width:183px">Sanitär und Bauklempnerei.</div>
      <div class="abs c white" style="top:71px;font-size:2.8px;line-height:3.8px">Bei uns sind Sie an der richtigen Stelle, wenn Sie auf der Suche nach<br>hochwertigen und facettenreichen Klempnerleistungen sind.</div>
      <div class="btn" style="left:99px;top:85px;width:40px;height:9px;line-height:9px;background:var(--white);color:var(--ink)">Mehr erfahren.</div>
      <span class="social" style="left:226px;top:93px;width:2.6px;height:2.6px"></span>
      <span class="social" style="left:226px;top:98px;width:2.6px;height:2.6px;border-radius:50%"></span>
      <span class="social" style="left:226px;top:103px;width:2.6px;height:2.6px"></span>
    </div>

    <div class="photo" role="img" aria-label="Foto: Frau wäscht sich die Hände am Küchenwasserhahn" style="left:99px;top:148px;width:119px;height:88px;background:linear-gradient(120deg,#8a8f96,#4b4f55 45%,#2a2c30)"></div>
    <div class="hbox" style="left:17px;top:155px;width:180px">Seit 1989 ist unser Leistungsspektrum, ebenso wie</div>
    <div class="hbox" style="left:17px;top:165px;width:153px">unser Qualitätsanspruch, stetig gewachsen.</div>
    <div class="tx" style="left:18px;top:178px;width:74px">
      <p>Neben den gängigen Klempnerarbeiten realisieren die Mitarbeiter unseres Familienunternehmens exklusive Sanitär- und Heizungsinstallationen sowie vielseitige Dachklempnerarbeiten. Darüber hinaus sind wir Ihr Ansprechpartner, wenn es um die Planung Ihrer Sanitärbereiche geht.</p>
      <p>Des Weiteren sind wir Ihr Partner für alternative Energien mit Solar, Erdwärme oder Holzöfen.</p>
    </div>

    <div class="photo" role="img" aria-label="Foto: Bad mit Glasdusche und schwarzem Waschtisch" style="left:20px;top:258px;width:91px;height:104px;background:linear-gradient(160deg,#d9d4cc,#b9b1a6 55%,#4b4743)"></div>
    <div class="ring" style="left:11px;top:306px">‹</div>
    <div class="ring" style="left:114px;top:306px">›</div>
    <div class="hd" style="left:130px;top:263px;font-size:6.6px">Ein Meisterbetrieb<br>mit Erfahrung und<br>Tradition</div>
    <div class="tx" style="left:130px;top:292px;width:92px">
      <p>Seit der Gründung im Jahr 1989 ist unser Meisterbetrieb in der Hand von Familie Wendlin. Wir sind Ihre Anlaufstelle für hochwertige Klempnerarbeiten in Heizung und Sanitär.</p>
      <p>Egal, ob Sie sich für alternative Energien oder Bäder nach Maß interessieren, bei uns erhalten Sie eine fachgerechte Durchführung und allumfassende Beratung. Unsere 14 kompetenten Mitarbeiter stehen Ihnen zur Seite.</p>
    </div>
    <div class="tag" style="left:158px;top:353px;width:76px">Wir vereinen Tradition</div>
    <div class="tag" style="left:188px;top:361px;width:46px">und Qualität</div>
    <div class="abs" style="left:62px;top:368px;display:flex;gap:.6px"><i style="width:1.6px;height:1.6px;border-radius:50%;background:var(--brand-blue);display:block"></i><i style="width:1.6px;height:1.6px;border-radius:50%;border:.3px solid var(--brand-blue);display:block"></i><i style="width:1.6px;height:1.6px;border-radius:50%;border:.3px solid var(--brand-blue);display:block"></i><i style="width:1.6px;height:1.6px;border-radius:50%;border:.3px solid var(--brand-blue);display:block"></i></div>

    <div class="band" style="top:386px;height:133px">
      <div class="photo" role="img" aria-label="Hintergrundbild: Badezimmer mit Fenster, blau getönt" style="left:0;top:0;width:234px;height:133px;background:linear-gradient(110deg,#4a5aa0,#3f528c 50%,#2f456a)"></div>
      <div class="abs c white" style="top:13px;font-size:6.4px;line-height:9px;letter-spacing:.12em">Unser facettenreiches<br>Leistungsspektrum für beste Qualität</div>
      <div class="abs" style="left:26px;top:39px;width:73px;height:81px;background:var(--white)"></div>
      <div class="photo" role="img" aria-label="Foto: helles Bad mit freistehender Wanne" style="left:26px;top:39px;width:73px;height:40px;background:linear-gradient(135deg,#e8e3dd,#c9c0b5)"></div>
      <div class="abs" style="left:26px;top:84px;width:73px;text-align:center;font-size:4.4px;line-height:5px;letter-spacing:.1em">Sanitär und Bäder<br>nach Maß</div>
      <div class="tx" style="left:32px;top:96px;width:61px;text-align:center;font-size:2.1px;line-height:2.8px">Ruhe, Entspannung, Erholung und Hygiene – das sind die Anforderungen an Ihr Badezimmer. Wir bieten Ihnen fachgerechte Lösungen rund um Ihren Sanitärbereich.</div>
      <div class="abs" style="left:99px;top:39px;width:91px;height:81px;background:rgba(255,255,255,.14)"></div>
      <div class="tx white" style="left:106px;top:44px;width:80px;font-size:2.2px;line-height:2.9px;color:var(--white)">
        <p>Unser Unternehmen bietet Ihnen:</p>
        <p style="font-weight:700">· den Neubau Ihrer Sanitäranlage<br>· Wartungsarbeiten<br>· Bäder nach Maß – auch bei ungewöhnlichen Grundrissen<br>· barrierefreie Bäder<br>· Ihre speziellen Wünsche<br>· ein umfangreiches Sanitär-Angebot<br>· Ideenfindung mit Fachmessen</p>
        <p>Kommen Sie mit Ihren Ideen zu uns, wir beraten Sie und besprechen gemeinsam alle Möglichkeiten für Ihren Rückzugsort.</p>
      </div>
      <div class="ring" style="left:12px;top:77px;border-color:var(--white);color:var(--white)">‹</div>
      <div class="ring" style="left:200px;top:77px;border-color:var(--white);color:var(--white)">›</div>
      <div class="side-tab" style="top:35px">Heizung</div>
      <div class="side-tab" style="top:40.5px">Sanitär und Bäder</div>
      <div class="side-tab" style="top:46px">Dachklempnerei</div>
      <div class="side-tab" style="top:51.5px">Alternative Energie</div>
      <div class="side-tab" style="top:57px">Solar</div>
      <div class="side-tab" style="top:62.5px">Service</div>
    </div>

    <div class="hd" style="left:18px;top:548px">Unsere Referenzen<br>sprechen für sich.</div>
    <div class="tx" style="left:18px;top:567px;width:86px;font-size:2.2px;line-height:3px">
      <p>Lorem ipsum dolor sit amet, consectetur adipiscing elit. Fusce quis quam non enim blandit tempor. Proin ac tellus accumsan leo sagittis.</p>
      <p>Lorem ipsum dolor sit amet, consectetur adipiscing elit. Fusce quis quam non enim blandit tempor. Proin ac tellus accumsan leo sagittis.</p>
    </div>
    <div class="photo" role="img" aria-label="Foto: Handwerker in Latzhose mit Klemmbrett" style="left:117px;top:534px;width:71px;height:91px;background:linear-gradient(180deg,#aab1b8,#5c6e93 60%,#2f3f78)"></div>
    <div class="photo" role="img" aria-label="Foto: Baustelle eines Rohbaus" style="left:171px;top:584px;width:49px;height:62px;background:linear-gradient(160deg,#8f96a3,#4c5566);border:1px solid var(--white)"></div>
    <div class="tag" style="left:0;top:627px;width:89px">“Lorem ipsum dolor</div>
    <div class="tag" style="left:0;top:637px;width:152px">sit amet, condipiscing elit fucas quia.</div>

    <div class="band" style="top:661px;height:72px">
      <div class="photo" role="img" aria-label="Hintergrundbild: Heizungsrohre, dunkel getönt" style="left:0;top:0;width:234px;height:72px;background:linear-gradient(100deg,var(--navy),#324a66 50%,var(--navy-deep))"></div>
      <div class="abs c white" style="top:14px;font-size:4.5px;letter-spacing:.2em">★★★★★</div>
      <div class="abs c white" style="top:24px;font-size:4.2px;line-height:5.3px;letter-spacing:.06em">“Vielen Dank an das ganze Team. Es wurde sich für<br>das Beratungsgespräch Zeit genommen,<br>alles pünktlich und sehr professionell umgesetzt.<br>Es war eine Freude.”</div>
      <div class="abs c white" style="top:54px;font-size:2.6px;letter-spacing:.1em">L. Berger</div>
    </div>

    <div class="photo" role="img" aria-label="Foto: Hausfassade mit Baum vor blauem Himmel" style="left:0;top:740px;width:61px;height:103px;background:linear-gradient(170deg,#6f9ad0,#8db0d6 50%,#4d6b3c)"></div>
    <div class="photo" role="img" aria-label="Foto: Hände bei der Montage von Solarmodulen" style="left:171px;top:765px;width:63px;height:99px;background:linear-gradient(160deg,#aeb6c2,#4a5f9c 55%,#243a86)"></div>
    <div class="hd" style="left:61px;top:761px;width:110px;text-align:center">Entdecken Sie unsere<br>aktuellen Beiträge.</div>
    <div class="tx" style="left:74px;top:786px;width:84px;text-align:center;font-size:2.2px;line-height:2.9px">Lorem ipsum dolor sit amet, consectetur adipiscing elit. Fusce quis quam non enim blandit tempor. Proin ac tellus accumsan leo sagittis.</div>
    <div class="btn" style="left:96px;top:813px;width:40px;height:9px;line-height:9px;background:var(--brand-blue);color:var(--white)">Zu den News.</div>

    <div class="band" style="top:872px;height:134px">
      <div class="photo" role="img" aria-label="Hintergrundbild: Hand mit Smartphone, blau getönt" style="left:0;top:0;width:234px;height:134px;background:linear-gradient(120deg,#4c6190,#36507a 50%,#22394f)"></div>
      <div class="hbox" style="left:0;top:26px;width:77px;background:var(--veil);color:var(--white);box-shadow:none;padding-left:12px">Wir freuen uns</div>
      <div class="hbox" style="left:0;top:37px;width:85px;background:var(--veil);color:var(--white);box-shadow:none;padding-left:12px">auf Ihre Anfrage.</div>
      <div class="tx" style="left:14px;top:53px;width:59px;font-size:2.2px;line-height:2.9px;color:var(--white)">Lorem ipsum dolor sit amet, consectetur adipiscing elit. Fusce quis quam non enim blandit tempor. Proin ac tellus accumsan leo sagittis. Lorem ipsum dolor sit amet, consectetur adipiscing elit.</div>
      <div class="field" style="left:93px;top:45px;width:38px;height:8px">Name</div>
      <div class="field" style="left:134px;top:45px;width:37px;height:8px">Nachname</div>
      <div class="field" style="left:93px;top:56px;width:78px;height:7px">E-Mail Adresse</div>
      <div class="field" style="left:174px;top:56px;width:33px;height:7px">Telefon</div>
      <div class="field" style="left:93px;top:66px;width:114px;height:27px">Nachricht</div>
      <div class="btn" style="left:93px;top:99px;width:39px;height:9px;line-height:8px;border:.5px solid var(--white);color:var(--white)">Kontaktieren.</div>
    </div>

    <div class="photo" role="img" aria-label="Stadtplan mit Standort des Betriebs" style="left:0;top:1006px;width:234px;height:48px;background:linear-gradient(100deg,#e6ebf0,#d6e3ee 50%,#e9ece6)"></div>

    <footer class="band" style="top:1054px;height:48px;background:linear-gradient(100deg,#2e4570,var(--navy-deep))">
      <div class="tx" style="left:14px;top:12px;width:50px;font-size:2.2px;line-height:3.2px;color:var(--white)">Wendlin GmbH<br><br>OT Talgrund<br>Wiesenweg 12<br>09000 Musterau</div>
      <div class="tx" style="left:72px;top:15px;width:60px;font-size:2.2px;line-height:3.2px;color:var(--white)">Tel.: 03700 123450<br>Fax: 03700 123451<br><br>E-Mail: info@heizung-wendlin.example</div>
      <div class="tx" style="left:14px;top:39px;width:120px;font-size:2.2px;letter-spacing:.15em;color:var(--white);display:flex;gap:16px"><span>Datenschutz</span><span>Impressum</span><span>Kontakt</span></div>
      <span class="abs" aria-label="Innungsmitgliedschaft" style="left:185px;top:9px;width:28px;height:28px;border-radius:50%;background:#f0c419;border:2px solid var(--white)"></span>
    </footer>
  </section>

  <!-- ============ desktop page ============ -->
  <section class="page desk" aria-label="Startseite Desktop">
    <header class="header">
      <div class="wordmark abs"><span class="dot"></span>wendlin</div>
      <div class="tagline">Heizung · Sanitär · Bauklempnerei</div>
      <nav>
        <span class="nav-item is-active" style="left:245px">HOME</span>
        <span class="nav-item" style="left:298px">ÜBER UNS</span>
        <span class="nav-item" style="left:374px">LEISTUNGEN</span>
        <span class="nav-item" style="left:454px">AKTUELL</span>
        <span class="nav-item" style="left:517px">REFERENZEN</span>
        <span class="nav-item" style="left:597px">KONTAKT</span>
      </nav>
      <div class="burger"><span></span><span></span><span></span></div>
    </header>

    <section class="hero">
      <div class="photo hero-photo" role="img" aria-label="Headerbild: modernes Badezimmer mit Waschtisch und Spiegel, blau getönt"></div>
      <div class="kicker">TRADITIONSREICHER FAMILIENBETRIEB:</div>
      <div class="title-line" style="left:135px;top:86px;width:411px">Willkommen bei wendlin</div>
      <div class="title-line" style="left:135px;top:126px;width:411px">Ihr Experte für Heizung,</div>
      <div class="title-line" style="left:112px;top:165px;width:476px">Sanitär und Bauklempnerei.</div>
      <p class="hero-sub">Bei uns sind Sie an der richtigen Stelle, wenn Sie auf der Suche nach<br>hochwertigen und facettenreichen Klempnerleistungen sind.</p>
      <div class="btn-hero">Mehr erfahren.</div>
      <span class="social" style="top:275px"></span>
      <span class="social" style="top:292px;border-radius:50%"></span>
      <span class="social" style="top:310px"></span>
    </section>

    <section class="intro">
      <div class="photo" role="img" aria-label="Foto: Frau wäscht sich die Hände unter einem Küchenwasserhahn" style="left:297px;top:445px;width:362px;height:267px;background:linear-gradient(120deg,#9a9ea4 0%,#5f6369 35%,#34373b 70%,#222427 100%)"></div>
      <div class="h-box" style="left:48px;top:463px;width:544px">Seit 1989 ist unser Leistungsspektrum, ebenso wie</div>
      <div class="h-box" style="left:48px;top:494px;width:467px">unser Qualitätsanspruch, stetig gewachsen.</div>
      <div class="body" style="left:55px;top:536px;width:222px">
        <p>Neben den gängigen Klempnerarbeiten realisieren die Mitarbeiter unseres Familien­unternehmens exklusive Sanitär- und Heizungsinstallationen sowie vielseitige Dachklempnerarbeiten. Darüber hinaus sind wir Ihr Ansprechpartner, wenn es um die Planung Ihrer Sanitärbereiche geht, damit Sie sich Ihr neues Badezimmer bereits vor dem Bau vorstellen können.</p>
        <p>Des Weiteren sind wir Ihr Partner für alternative Energien. Mit einer hohen Fachkompetenz statten wir Ihr Haus mit Solar, Erdwärme oder Holzöfen aus, um nicht nur die Umwelt, sondern auch Ihren Geldbeutel zu schonen.</p>
      </div>
      <div class="divider"></div>
    </section>

    <section class="meister">
      <div class="photo" role="img" aria-label="Foto: Badezimmer mit schwarz gerahmter Glasdusche und Waschtisch" style="left:60px;top:776px;width:273px;height:314px;background:linear-gradient(165deg,#e2ddd6 0%,#cfc8bf 45%,#9d968d 75%,#3d3a37 100%)"></div>
      <svg class="arrow" style="left:32px;top:919px" viewBox="0 0 22 22" aria-hidden="true"><circle cx="11" cy="11" r="10.3" fill="none" stroke="#2b2b2b" stroke-width="1"/><path d="M15 11H7M10 8l-3 3 3 3" fill="none" stroke="#2b2b2b" stroke-width="1"/></svg>
      <svg class="arrow" style="left:342px;top:919px" viewBox="0 0 22 22" aria-hidden="true"><circle cx="11" cy="11" r="10.3" fill="none" stroke="#2b2b2b" stroke-width="1"/><path d="M7 11h8M12 8l3 3-3 3" fill="none" stroke="#2b2b2b" stroke-width="1"/></svg>
      <h2 class="h-meister" style="font-weight:400">Ein Meisterbetrieb<br>mit Erfahrung und<br>Tradition</h2>
      <div class="body" style="left:392px;top:879px;width:282px">
        <p>Seit der Gründung im Jahr 1989 ist unser Meisterbetrieb in der Hand von Familie Wendlin. Wir sind Ihre Anlaufstelle für hochwertige und facettenreiche Klempnerarbeiten.<br>Mit einem hohen Fachwissen und einem exzellenten Qualitätsbewusstsein realisieren wir vielfältige Arbeiten im Bereich Heizung und Sanitär.</p>
        <p>Egal, ob Sie sich für alternative Energien oder Bäder nach Maß interessieren, bei uns erhalten Sie nicht nur eine fachgerechte Durchführung Ihrer Wünsche, sondern auch eine allumfassende Beratung. Unsere 14 kompetenten Mitarbeiter stehen Ihnen während des gesamten Bauprozesses und auch darüber hinaus zur Seite und sind von der Planung bis zur regelmäßigen Wartung der Anlagen für Sie da.</p>
      </div>
      <div class="tag" style="left:473px;top:1059px;width:231px">Wir vereinen Tradition</div>
      <div class="tag" style="left:564px;top:1085px;width:140px">und Qualität</div>
      <div class="dots"><i class="on"></i><i></i><i></i><i></i><i></i></div>
    </section>
  </section>

</div>
</body>
</html>
```